Action Camera Rental Website, with add on video editing service

I'm looking for a new website, which I will be able to administer once complete which will list camera equipment for rental. There are some key features I would like which I have not been able to add on any proprietary site builders (see brief, reference to availability and booking system)
The website must have functionality to select products and check availability for their hire / rental. I would like the functionality to specify (for example), hire from 2nd to 9th, then the equipment arrival date will be 1st, return date will be 10th. See brief for link to similar page.
Website should be simple and quick to use.It should include FAQ page, to allow me to modify with questions . answers to limit the amount of questions I have to answer via email. I would also like a blog page to post videos made by or for our users.
I would also be interested in the functionality for users to upload their footage to a FTP site (or similar) for us to edit.

Target Market(s)

Young, adventurous people/ Action sports, holiday companies

Industry/Entity Type

Videography

Number of Pages Required

5+ page

Requirements
Must have
• Hire / Booking page, which checks availability of selected equipment. Be modifiable by me. Ability to add new products without needing support
Nice to have
• Vibrant, adventurous layout and colour scheme.

```html
<!DOCTYPE html>
<html lang="en">
<head>
<meta charset="utf-8">
<title>Reel Rush – Action Camera Rental</title>
<link rel="stylesheet" href="https://fonts.googleapis.com/css2?family=Open+Sans:wght@400;600;700&display=swap">
<style>
:root{
  --ink:#222;
  --text:#555;
  --muted:#888;
  --white:#fff;
  --accent:#5bc4f1;
  --price:#e8434b;
  --star:#f2b01e;
  --panel:#efefef;
  --field:#2f2f2f;
  --card-band:#f4f4f4;
  --line:#e3e3e3;
  --footer:#2b2b2b;
  --icon:#9a9a9a;
}
*{box-sizing:border-box;margin:0;padding:0}
html,body{width:1200px;height:3051px;overflow:hidden}
body{position:relative;font-family:"Open Sans",Arial,sans-serif;color:var(--text);background:var(--white)}
.abs{position:absolute}

/* hero */
.hero{left:0;top:0;width:1200px;height:661px;
  background:
    radial-gradient(ellipse 260px 90px at 470px 470px,rgba(220,60,110,.55),rgba(220,60,110,0)),
    radial-gradient(ellipse 170px 220px at 430px 330px,rgba(60,150,130,.55),rgba(60,150,130,0)),
    radial-gradient(ellipse 420px 330px at 1050px 230px,#1d2a22 0%,rgba(29,42,34,.85) 45%,rgba(29,42,34,0) 100%),
    radial-gradient(ellipse 200px 260px at 40px 150px,rgba(30,42,34,.9),rgba(30,42,34,0)),
    linear-gradient(180deg,#12307a 0%,#2a56a8 22%,#7d98bf 36%,#c9d3df 50%,#e6ebf2 68%,#f3f5f9 100%)}
.hero-shade{left:0;top:0;width:1200px;height:661px;background:linear-gradient(180deg,rgba(0,0,0,.1) 0%,rgba(0,0,0,.05) 30%,rgba(20,30,50,.38) 50%,rgba(20,30,50,.3) 66%,rgba(0,0,0,.05) 85%)}
.logo{left:98px;top:6px;width:168px;height:168px;border-radius:50%;background:var(--white);display:flex;align-items:center;justify-content:center;text-align:center;font-size:30px;line-height:1.15;font-weight:400;color:var(--ink);letter-spacing:1px}
.nav a{position:absolute;top:82px;white-space:nowrap;font-size:14px;font-weight:600;color:var(--white);text-decoration:none;letter-spacing:.2px}
.hero-title{left:0;top:338px;width:1200px;text-align:center;font-size:38px;font-weight:400;color:var(--white);letter-spacing:1px;text-shadow:0 1px 3px rgba(0,0,0,.4)}
.hero-sub{left:150px;top:400px;width:900px;text-align:center;font-size:14.5px;line-height:24px;color:var(--white);text-shadow:0 1px 2px rgba(0,0,0,.55)}
.dots{display:flex;gap:10px}
.dots span{width:14px;height:14px;border-radius:50%;background:var(--white);border:2px solid var(--white)}
.dots span.on{background:transparent}

/* feature tiles */
.tile{top:667px;height:218px;display:flex;flex-direction:column;align-items:center;color:var(--white);text-align:center;overflow:hidden}
.tile h3{position:relative;margin-top:72px;font-size:14px;font-weight:600;letter-spacing:.3px;text-shadow:0 1px 2px rgba(0,0,0,.4)}
.tile p{position:relative;margin-top:14px;font-size:14px;line-height:19px;width:320px;text-shadow:0 1px 2px rgba(0,0,0,.4)}
.tile .play{position:absolute;left:50%;top:98px;transform:translateX(-50%)}
.t1{left:0;width:397px;background:
  radial-gradient(ellipse 140px 120px at 80px 180px,rgba(255,255,255,.55),rgba(255,255,255,0)),
  radial-gradient(ellipse 200px 160px at 330px 60px,#0a3848,rgba(10,56,72,0)),
  linear-gradient(135deg,#0b4f63 0%,#167f97 45%,#4fb5c8 75%,#cfe9ee 100%)}
.t2{left:401px;width:397px;background:
  radial-gradient(ellipse 120px 90px at 360px 40px,rgba(255,255,255,.8),rgba(255,255,255,0)),
  linear-gradient(180deg,#2f66b6 0%,#6d9fd6 40%,#cfdcec 62%,#f2f5f9 80%,#dfe6ef 100%)}
.t3{left:803px;width:397px;background:
  radial-gradient(circle 60px at 140px 30px,#fff3c0 0%,#ffd26a 30%,rgba(255,170,60,0) 100%),
  radial-gradient(ellipse 110px 120px at 70px 130px,#1c130d,rgba(28,19,13,0)),
  linear-gradient(180deg,#2e2a3a 0%,#a8582a 32%,#f0a23a 58%,#7a4b24 78%,#231811 100%)}
.arrow{top:768px}

/* welcome */
.welcome-frame{left:177px;top:997px;width:325px;height:278px;border:1px solid #999}
.welcome-photo{left:142px;top:980px;width:328px;height:273px;background:
  radial-gradient(ellipse 90px 110px at 120px 120px,rgba(40,40,45,.7),rgba(40,40,45,0)),
  radial-gradient(ellipse 180px 80px at 300px 60px,rgba(255,250,220,.8),rgba(255,250,220,0)),
  linear-gradient(180deg,#2c6fbf 0%,#79b1e2 40%,#c9d8d8 56%,#9a8a55 66%,#6e6436 82%,#4e4828 100%)}
.welcome-copy{left:535px;top:1010px;width:532px}
.welcome-copy h2{font-size:26px;font-weight:400;color:var(--ink);letter-spacing:.2px}
.welcome-copy h4{margin-top:4px;font-size:17px;font-weight:400;color:var(--ink)}
.welcome-copy p{margin-top:12px;font-size:12.5px;line-height:23px;color:var(--text);text-align:justify}
.welcome-copy p+p{margin-top:6px}
.btn-read{display:inline-block;margin-top:12px;width:118px;height:33px;border-radius:17px;background:var(--accent);color:var(--white);font-size:12px;line-height:33px;text-align:center;letter-spacing:.3px}

/* hire */
.hire{left:0;top:1357px;width:1200px;height:1009px;background:var(--panel)}
.section-title{left:0;width:1200px;text-align:center;font-size:33px;font-weight:700;color:var(--ink);letter-spacing:.5px}
.field{top:1485px;height:51px;background:var(--field);color:var(--white);font-size:13px;display:flex;align-items:center;justify-content:space-between;padding:0 16px}
.btn-hire{top:1485px;left:913px;width:137px;height:51px;background:var(--accent);color:var(--white);font-size:15px;font-weight:600;display:flex;align-items:center;justify-content:center;gap:8px}
.card{width:228px;height:319px;background:var(--white);box-shadow:0 1px 4px rgba(0,0,0,.12)}
.card .shot{height:190px;background:var(--shot)}
.card .name{height:36px;background:var(--card-band);font-size:13px;color:var(--text);display:flex;align-items:center;justify-content:center}
.card .meta{height:42px;display:flex;align-items:center;justify-content:space-between;padding:0 14px;border-bottom:1px solid var(--line)}
.card .price{font-size:16px;color:var(--price)}
.card .tools{height:51px;display:flex;color:var(--icon);fill:var(--icon)}
.card .tools span{flex:1;display:flex;align-items:center;justify-content:center;border-right:1px solid var(--line)}
.card .tools span:last-child{border-right:0}
.shot-silver{--shot:radial-gradient(ellipse 70px 58px at 50% 52%,#3c4148 0%,#8a9098 40%,#d4d8dc 70%,rgba(255,255,255,0) 100%),linear-gradient(180deg,#fff,#f3f4f5)}
.shot-black{--shot:radial-gradient(ellipse 46px 80px at 50% 52%,#1e2124 0%,#4a4e53 45%,#c3c6c9 75%,rgba(255,255,255,0) 100%),linear-gradient(180deg,#fff,#f3f4f5)}
.shot-cube{--shot:radial-gradient(ellipse 100px 48px at 50% 55%,#141516 0%,#3b2a2a 40%,#b9b3b3 72%,rgba(255,255,255,0) 100%),linear-gradient(180deg,#fff,#f3f4f5)}
.shot-kit{--shot:radial-gradient(ellipse 90px 50px at 50% 55%,#2a2d31 0%,#7e858c 45%,#d6dadd 72%,rgba(255,255,255,0) 100%),linear-gradient(180deg,#fff,#f3f4f5)}
.shot-white{--shot:radial-gradient(ellipse 80px 44px at 50% 52%,#5a6068 0%,#b7bcc2 45%,#e9ecef 72%,rgba(255,255,255,0) 100%),linear-gradient(180deg,#fff,#f3f4f5)}
.shot-frame{--shot:radial-gradient(ellipse 56px 62px at 50% 50%,#1d2024 0%,#4d535a 45%,#c8cbce 74%,rgba(255,255,255,0) 100%),linear-gradient(180deg,#fff,#f3f4f5)}
.shot-grey{--shot:radial-gradient(ellipse 72px 50px at 50% 52%,#33373c 0%,#7d8188 40%,#cfd2d6 72%,rgba(255,255,255,0) 100%),linear-gradient(180deg,#fff,#f3f4f5)}
.shot-mount{--shot:radial-gradient(ellipse 52px 78px at 50% 50%,#121314 0%,#3e4246 45%,#c4c6c8 74%,rgba(255,255,255,0) 100%),linear-gradient(180deg,#fff,#f3f4f5)}
.pager{display:flex;gap:6px}
.pager span{width:8px;height:8px;border-radius:50%;background:#888}
.pager span.on{background:var(--accent)}

/* blog */
.post{top:2502px;width:305px;height:285px;background:var(--white);box-shadow:0 1px 5px rgba(0,0,0,.15);text-align:center}
.post .pic{height:163px}
.post .date{position:absolute;left:0;top:92px;width:40px}
.post .date b{display:block;height:46px;background:var(--accent);color:var(--white);font-size:15px;font-weight:400;line-height:18px;padding-top:6px}
.post .date b small{display:block;font-size:8px}
.post .date i{display:block;height:26px;background:#333;color:var(--white);font-style:normal;font-size:11px;line-height:26px}
.post h3{margin-top:22px;font-size:16px;font-weight:400;color:var(--ink)}
.post p{margin:8px 26px 0;font-size:10.5px;line-height:18px;color:var(--muted)}
.post .more{display:block;margin-top:8px;font-size:11px;color:var(--ink)}

/* footer */
.footer{left:0;top:2858px;width:1200px;height:193px;background:var(--footer);color:var(--white);text-align:center}
.footer-links{margin-top:58px;font-size:11px;letter-spacing:.3px}
.footer-links span{margin:0 8px}
.social{margin-top:14px;display:flex;justify-content:center;gap:10px}
.social span{width:24px;height:24px;border-radius:50%;border:1.5px solid var(--white);display:flex;align-items:center;justify-content:center}
.copy{margin-top:12px;font-size:11px}
</style>
</head>
<body>

<svg width="0" height="0" style="position:absolute" aria-hidden="true">
  <defs>
    <symbol id="star" viewBox="0 0 20 20"><path d="M10 1l2.7 5.8 6.3.7-4.7 4.3 1.3 6.2L10 14.9 4.4 18l1.3-6.2L1 7.5l6.3-.7z"/></symbol>
    <symbol id="cart" viewBox="0 0 20 20"><path d="M1 3h3l2.2 9h9.3l2-7H5.2" fill="none" stroke="currentColor" stroke-width="2"/><circle cx="7.5" cy="16" r="1.6"/><circle cx="14.5" cy="16" r="1.6"/></symbol>
    <symbol id="heart" viewBox="0 0 20 20"><path d="M10 17S2 11.5 2 6.5A4 4 0 0 1 10 5a4 4 0 0 1 8 1.5C18 11.5 10 17 10 17z"/></symbol>
    <symbol id="swap" viewBox="0 0 20 20"><path d="M3 7h12l-3-3M17 13H5l3 3" fill="none" stroke="currentColor" stroke-width="2"/></symbol>
    <symbol id="clock" viewBox="0 0 20 20"><circle cx="10" cy="10" r="7.5" fill="none" stroke="currentColor" stroke-width="1.8"/><path d="M10 6v4.5h3" fill="none" stroke="currentColor" stroke-width="1.8"/></symbol>
    <symbol id="cal" viewBox="0 0 20 20"><rect x="2" y="4" width="16" height="14" fill="none" stroke="currentColor" stroke-width="1.6"/><path d="M2 8h16M6 2v4M14 2v4M5 11h2M9 11h2M13 11h2M5 14h2M9 14h2" stroke="currentColor" stroke-width="1.6"/></symbol>
    <symbol id="play" viewBox="0 0 40 40"><circle cx="20" cy="20" r="19" fill="rgba(0,0,0,.6)"/><path d="M15 12l13 8-13 8z" fill="#fff"/></symbol>
    <symbol id="rating" viewBox="0 0 90 16">
      <use href="#star" x="0" width="16" height="16" fill="#f2b01e"/>
      <use href="#star" x="18" width="16" height="16" fill="#f2b01e"/>
      <use href="#star" x="36" width="16" height="16" fill="#f2b01e"/>
      <use href="#star" x="54" width="16" height="16" fill="#f2d58a"/>
      <use href="#star" x="72" width="16" height="16" fill="none" stroke="#f2b01e" stroke-width="1.2"/>
    </symbol>
    <symbol id="tools" viewBox="0 0 228 51">
      <use href="#cart" x="49" y="18" width="16" height="16"/>
      <use href="#heart" x="106" y="18" width="16" height="16"/>
      <use href="#swap" x="163" y="18" width="16" height="16"/>
      <use href="#clock" x="220" y="18" width="16" height="16"/>
    </symbol>
  </defs>
</svg>

<!-- Hero -->
<header>
  <div class="abs hero" role="img" aria-label="Snowboarder carving down a groomed snowy slope under a deep blue sky with pine trees"></div>
  <div class="abs hero-shade"></div>
  <div class="abs logo">REEL<br>RUSH</div>
  <nav class="nav">
    <a class="abs" style="left:598px">THE STORE</a>
    <a class="abs" style="left:742px">TIPS AND TRICKS</a>
    <a class="abs" style="left:932px">THE BLOG</a>
    <a class="abs" style="left:1072px">FAQ</a>
  </nav>
  <h1 class="abs hero-title">WE ARE AN ACTION CAMERA RENTAL COMPANY</h1>
  <p class="abs hero-sub">Sed ut perspiciatis unde omnis iste natus error sit voluptatem accusantium doloremque laudantium, totam rem aperiam,<br>eaque ipsa quae ab illo inventore veritatis et quasi architecto beatae.</p>
  <div class="abs dots" style="left:555px;top:611px"><span class="on"></span><span></span><span></span><span></span></div>
</header>

<!-- Feature tiles -->
<section>
  <div class="abs tile t1" role="img" aria-label="Surfer riding inside a turquoise wave">
    <h3>CILLUM DOLORE EU FUGIAT NULLA</h3>
    <p>Ut enim ad minima veniam, quis nostrum exercitationem ullam corporis</p>
    <svg class="play" width="32" height="32"><use href="#play"/></svg>
  </div>
  <div class="abs tile t2" role="img" aria-label="Skier on a snowy mountain slope under blue sky">
    <h3>ARCHITECTO BEATAE VITAE DICTA</h3>
    <p>Nemo enim ipsam voluptatem quia voluptas sit aspernatur aut odit aut fugit</p>
    <svg class="play" width="32" height="32"><use href="#play"/></svg>
  </div>
  <div class="abs tile t3" role="img" aria-label="Photographer silhouetted against a golden sunset">
    <h3>OCCAECAT CUPIDATAT NON PROID</h3>
    <p>Sunt in culpa qui officia deserunt mollit anim id est laborum</p>
    <svg class="play" width="32" height="32"><use href="#play"/></svg>
  </div>
  <svg class="abs arrow" style="left:12px" width="14" height="26"><path d="M12 2L2 13l10 11" fill="none" stroke="#fff" stroke-width="2"/></svg>
  <svg class="abs arrow" style="left:1174px" width="14" height="26"><path d="M2 2l10 11L2 24" fill="none" stroke="#fff" stroke-width="2"/></svg>
</section>

<!-- Welcome -->
<section>
  <div class="abs welcome-frame"></div>
  <div class="abs welcome-photo" role="img" aria-label="Action camera on a tripod overlooking a sunny hillside"></div>
  <div class="abs welcome-copy">
    <h2>WELCOME TO REEL RUSH</h2>
    <h4>I am an amateur, but a quick learner.</h4>
    <p>I have an amateur's experience of using TrailCam's and the associated equipment to create vacation movies. Had I not enjoyed the editing process, I'd have given up way before having anything watchable. As it is, we revisit our videos all the time, we almost never look back at our photos.</p>
    <p>I've not written or run a website before, so you may need to be patient with me.</p>
    <span class="btn-read">READ MORE</span>
  </div>
</section>

<!-- Hire -->
<section>
  <div class="abs hire"></div>
  <h2 class="abs section-title" style="top:1404px">HIRE PRODUCT YOU NEED</h2>

  <div class="abs field" style="left:151px;width:197px">Product Category <svg width="10" height="6"><path d="M1 1l4 4 4-4" fill="none" stroke="#fff" stroke-width="1.4"/></svg></div>
  <div class="abs field" style="left:380px;width:157px">Keyword <svg width="10" height="6"><path d="M1 1l4 4 4-4" fill="none" stroke="#fff" stroke-width="1.4"/></svg></div>
  <div class="abs field" style="left:570px;width:138px">Hire from <svg width="13" height="13" style="color:#fff"><use href="#cal"/></svg></div>
  <div class="abs field" style="left:740px;width:139px">Hire to <svg width="13" height="13" style="color:#fff"><use href="#cal"/></svg></div>
  <div class="abs btn-hire">HIRE NOW <svg width="8" height="12"><path d="M1 1l5 5-5 5" fill="none" stroke="#fff" stroke-width="2"/></svg></div>

  <div class="abs card" style="left:114px;top:1601px">
    <div class="shot shot-silver" role="img" aria-label="Silver action camera in a housing"></div>
    <div class="name">Product Name</div>
    <div class="meta"><span class="price">$76.00</span><svg width="86" height="15"><use href="#rating"/></svg></div>
    <div class="tools"><span><svg width="16" height="16"><use href="#cart"/></svg></span><span><svg width="16" height="16"><use href="#heart"/></svg></span><span><svg width="16" height="16"><use href="#swap"/></svg></span><span><svg width="16" height="16"><use href="#clock"/></svg></span></div>
  </div>
  <div class="abs card" style="left:362px;top:1601px">
    <div class="shot shot-black" role="img" aria-label="Black action camera on a handheld grip"></div>
    <div class="name">Product Name</div>
    <div class="meta"><span class="price">$76.00</span><svg width="86" height="15"><use href="#rating"/></svg></div>
    <div class="tools"><span><svg width="16" height="16"><use href="#cart"/></svg></span><span><svg width="16" height="16"><use href="#heart"/></svg></span><span><svg width="16" height="16"><use href="#swap"/></svg></span><span><svg width="16" height="16"><use href="#clock"/></svg></span></div>
  </div>
  <div class="abs card" style="left:608px;top:1601px">
    <div class="shot shot-cube" role="img" aria-label="Two compact cube action cameras"></div>
    <div class="name">Product Name</div>
    <div class="meta"><span class="price">$76.00</span><svg width="86" height="15"><use href="#rating"/></svg></div>
    <div class="tools"><span><svg width="16" height="16"><use href="#cart"/></svg></span><span><svg width="16" height="16"><use href="#heart"/></svg></span><span><svg width="16" height="16"><use href="#swap"/></svg></span><span><svg width="16" height="16"><use href="#clock"/></svg></span></div>
  </div>
  <div class="abs card" style="left:856px;top:1601px">
    <div class="shot shot-kit" role="img" aria-label="Action camera kit with housing and remote"></div>
    <div class="name">Product Name</div>
    <div class="meta"><span class="price">$76.00</span><svg width="86" height="15"><use href="#rating"/></svg></div>
    <div class="tools"><span><svg width="16" height="16"><use href="#cart"/></svg></span><span><svg width="16" height="16"><use href="#heart"/></svg></span><span><svg width="16" height="16"><use href="#swap"/></svg></span><span><svg width="16" height="16"><use href="#clock"/></svg></span></div>
  </div>

  <div class="abs card" style="left:114px;top:1949px">
    <div class="shot shot-white" role="img" aria-label="White action camera in a clear housing"></div>
    <div class="name">Product Name</div>
    <div class="meta"><span class="price">$76.00</span><svg width="86" height="15"><use href="#rating"/></svg></div>
    <div class="tools"><span><svg width="16" height="16"><use href="#cart"/></svg></span><span><svg width="16" height="16"><use href="#heart"/></svg></span><span><svg width="16" height="16"><use href="#swap"/></svg></span><span><svg width="16" height="16"><use href="#clock"/></svg></span></div>
  </div>
  <div class="abs card" style="left:362px;top:1949px">
    <div class="shot shot-frame" role="img" aria-label="Cube action camera in a mounting frame"></div>
    <div class="name">Product Name</div>
    <div class="meta"><span class="price">$76.00</span><svg width="86" height="15"><use href="#rating"/></svg></div>
    <div class="tools"><span><svg width="16" height="16"><use href="#cart"/></svg></span><span><svg width="16" height="16"><use href="#heart"/></svg></span><span><svg width="16" height="16"><use href="#swap"/></svg></span><span><svg width="16" height="16"><use href="#clock"/></svg></span></div>
  </div>
  <div class="abs card" style="left:608px;top:1949px">
    <div class="shot shot-grey" role="img" aria-label="Grey action camera with front screen"></div>
    <div class="name">Product Name</div>
    <div class="meta"><span class="price">$76.00</span><svg width="86" height="15"><use href="#rating"/></svg></div>
    <div class="tools"><span><svg width="16" height="16"><use href="#cart"/></svg></span><span><svg width="16" height="16"><use href="#heart"/></svg></span><span><svg width="16" height="16"><use href="#swap"/></svg></span><span><svg width="16" height="16"><use href="#clock"/></svg></span></div>
  </div>
  <div class="abs card" style="left:856px;top:1949px">
    <div class="shot shot-mount" role="img" aria-label="Action camera on a suction cup mount"></div>
    <div class="name">Product Name</div>
    <div class="meta"><span class="price">$76.00</span><svg width="86" height="15"><use href="#rating"/></svg></div>
    <div class="tools"><span><svg width="16" height="16"><use href="#cart"/></svg></span><span><svg width="16" height="16"><use href="#heart"/></svg></span><span><svg width="16" height="16"><use href="#swap"/></svg></span><span><svg width="16" height="16"><use href="#clock"/></svg></span></div>
  </div>

  <div class="abs pager" style="left:583px;top:2315px"><span class="on"></span><span></span><span></span></div>
</section>

<!-- Blog -->
<section>
  <h2 class="abs section-title" style="top:2432px;font-weight:400;font-size:29px">LATEST BLOG</h2>

  <article class="abs post" style="left:116px">
    <div class="pic" role="img" aria-label="Kitesurfer on a sunny blue sea" style="background:radial-gradient(ellipse 60px 80px at 200px 100px,rgba(120,70,40,.75),rgba(120,70,40,0)),radial-gradient(ellipse 120px 50px at 80px 20px,rgba(255,255,240,.9),rgba(255,255,240,0)),linear-gradient(180deg,#8fc2e6 0%,#d6e6ee 42%,#3a98c0 58%,#1f6f95 78%,#b89470 100%)"></div>
    <div class="date"><b>02<small>JUN</small></b><i>2017</i></div>
    <h3>NEQUE PORRO QUISQUAM</h3>
    <p>It has survived not only five centuries, but also the leap into electronic typesetting, remaining</p>
    <span class="more">Read More »</span>
  </article>
  <article class="abs post" style="left:447px">
    <div class="pic" role="img" aria-label="Traveller holding a camera in an autumn forest" style="background:radial-gradient(ellipse 70px 110px at 150px 90px,rgba(40,34,30,.85),rgba(40,34,30,0)),radial-gradient(ellipse 90px 60px at 260px 30px,rgba(220,150,70,.7),rgba(220,150,70,0)),linear-gradient(180deg,#e0d2b8 0%,#a88a64 40%,#6a5036 70%,#332820 100%)"></div>
    <div class="date"><b>02<small>JUN</small></b><i>2017</i></div>
    <h3>NEQUE PORRO QUISQUAM</h3>
    <p>It has survived not only five centuries, but also the leap into electronic typesetting, remaining</p>
    <span class="more">Read More »</span>
  </article>
  <article class="abs post" style="left:779px">
    <div class="pic" role="img" aria-label="Hands holding a camera up against a cloudy sky" style="background:radial-gradient(ellipse 110px 50px at 150px 120px,rgba(170,80,200,.9),rgba(170,80,200,0)),radial-gradient(ellipse 120px 50px at 140px 50px,rgba(235,238,245,.8),rgba(235,238,245,0)),linear-gradient(180deg,#3f64a3 0%,#8fa4c8 45%,#b7a6d2 70%,#8c5fb8 100%)"></div>
    <div class="date"><b>02<small>JUN</small></b><i>2017</i></div>
    <h3>NEQUE PORRO QUISQUAM</h3>
    <p>It has survived not only five centuries, but also the leap into electronic typesetting, remaining</p>
    <span class="more">Read More »</span>
  </article>
</section>

<!-- Footer -->
<footer class="abs footer">
  <div class="footer-links"><span>ABOUT</span>|<span>PRIVACY</span>|<span>TERMS</span>|<span>LEGAL</span>|<span>CONTACT</span></div>
  <div class="social">
    <span aria-label="Share"><svg width="12" height="12" viewBox="0 0 12 12"><circle cx="9" cy="2.5" r="1.6" fill="#fff"/><circle cx="3" cy="6" r="1.6" fill="#fff"/><circle cx="9" cy="9.5" r="1.6" fill="#fff"/><path d="M9 2.5L3 6l6 3.5" fill="none" stroke="#fff" stroke-width="1"/></svg></span>
    <span aria-label="Chat"><svg width="12" height="12" viewBox="0 0 12 12"><path d="M1 2h10v6H5l-3 2.5V8H1z" fill="#fff"/></svg></span>
    <span aria-label="Like"><svg width="11" height="11" viewBox="0 0 20 20" fill="#fff"><use href="#heart"/></svg></span>
    <span aria-label="Website"><svg width="12" height="12" viewBox="0 0 12 12" fill="none" stroke="#fff" stroke-width="1.1"><circle cx="6" cy="6" r="4.8"/><ellipse cx="6" cy="6" rx="2" ry="4.8"/><path d="M1.2 6h9.6"/></svg></span>
    <span aria-label="Phone"><svg width="12" height="12" viewBox="0 0 12 12"><path d="M3 1l2 2.5-1.2 1.3a6 6 0 0 0 3.4 3.4L8.5 7 11 9l-1.2 1.8C5.5 11 1 6.5 1.2 2.2z" fill="#fff"/></svg></span>
    <span aria-label="Email"><svg width="12" height="10" viewBox="0 0 12 10" fill="none" stroke="#fff" stroke-width="1.1"><rect x=".6" y=".6" width="10.8" height="8.8"/><path d="M.6 .8L6 5.5 11.4.8"/></svg></span>
  </div>
  <div class="copy">Copyright © 2017 &nbsp;All Rights Reserved</div>
</footer>

</body>
</html>
```